Business Card design for an International Import Export House

We need a Business Card design for our import export business. We trade in Minerals, Metals, Rice, Sugar, Steel etc.. The design should be minimalistic. It may or may not contain the physical address. In case you want to include the physical address - 418 Verandah Heights, Marlow Sector 9, Gurgaon, Haryana, India, 122009.

Target Market(s)

Steel Mills or Steel Plants, Factories, Mining businesses, Industrial houses, Government Agencies

Industry/Entity Type

Importer

Contact Information for Business Card

Business Name - Tessan Overseas

Font styles to use
Other font styles liked:
• montserrat

Requirements
Must have
• Ravi Kandola - President
• www.tessanoverseas.com
• ravi@tessanoverseas.com
• +91-987-654-3217
Nice to have
• worldwide suppliers of ores

```html
<!DOCTYPE html>
<html lang="en">
<head>
<meta charset="utf-8">
<title>Tessan Overseas — Business Card</title>
<link href="https://fonts.googleapis.com/css2?family=Montserrat:wght@400;500;600;700&display=swap" rel="stylesheet">
<style>
  :root {
    --backdrop: #e9e4dc;
    --card: #23292e;
    --card-edge: #1a1f23;
    --teal: #4aaebe;
    --teal-deep: #3a97a6;
    --white: #f2f4f5;
    --soft-white: #d9dee1;
    --rule: #e6eaec;
  }
  * { box-sizing: border-box; margin: 0; padding: 0; }
  html, body {
    width: 1200px; height: 780px; overflow: hidden;
    background: var(--backdrop);
    font-family: "Montserrat", sans-serif;
  }
  .stage {
    width: 1200px; height: 780px;
    display: flex; justify-content: center; align-items: center; gap: 90px;
  }
  .card {
    position: relative;
    width: 354px; height: 620px;
    background: var(--card);
    border-radius: 4px;
    box-shadow: 0 14px 30px rgba(0,0,0,.22);
    overflow: hidden;
    display: flex; flex-direction: column; align-items: center;
    color: var(--white);
  }
  .card-band {
    position: absolute; left: 0; right: 0; bottom: 0;
    height: 64px;
    background: var(--teal);
    border-top: 6px solid var(--rule);
    box-shadow: 0 -3px 0 var(--card);
    display: flex; align-items: center; justify-content: center;
  }
  .card-band .website {
    font-size: 15px; font-weight: 500; letter-spacing: .6px;
    color: var(--white);
  }

  /* Brand lockup */
  .brand-lockup {
    display: flex; align-items: center; gap: 10px;
  }
  .brand-dot {
    width: 14px; height: 14px; border-radius: 50%;
    background: var(--teal);
  }
  .brand-name {
    font-weight: 700; color: var(--teal);
    letter-spacing: 1px; text-transform: uppercase;
  }

  /* Contact card */
  .contact-card .brand-lockup { margin-top: 92px; }
  .contact-card .brand-name { font-size: 20px; }
  .person-name {
    margin-top: 58px;
    font-size: 22px; font-weight: 700; letter-spacing: 1.2px;
    text-transform: uppercase;
  }
  .person-name .first { color: var(--teal); }
  .person-name .last { color: var(--white); }
  .person-role {
    margin-top: 2px; font-size: 15px; font-weight: 500; color: var(--soft-white);
  }
  .address {
    margin-top: 26px;
    font-size: 15px; font-weight: 500; line-height: 1.45;
    text-align: center; color: var(--white);
  }
  .divider {
    width: 240px; height: 1px; background: var(--teal-deep);
    margin: 18px 0 12px;
  }
  .contact-label {
    font-size: 14px; font-weight: 500; color: var(--teal);
  }
  .contact-value {
    font-size: 15px; font-weight: 500; letter-spacing: .4px; color: var(--white);
    margin-bottom: 8px;
  }
  .divider.lower { margin: 6px 0 0; }

  /* Brand card */
  .brand-card .brand-lockup { margin-top: 250px; }
  .brand-card .brand-name { font-size: 27px; }
</style>
</head>
<body>
  <main class="stage">
    <section class="card contact-card" aria-label="Contact side">
      <div class="brand-lockup">
        <span class="brand-dot"></span>
        <span class="brand-name">Tessan Overseas</span>
      </div>
      <h1 class="person-name"><span class="first">Ravi</span> <span class="last">Kandola</span></h1>
      <p class="person-role">President</p>
      <p class="address">418 Verandah Heights<br>Marlow Sector 9, Gurgaon<br>Haryana, India, 122009.</p>
      <div class="divider"></div>
      <p class="contact-label">Phone</p>
      <p class="contact-value">+91-987-654-3217</p>
      <p class="contact-label">Email</p>
      <p class="contact-value">ravi@tessanoverseas.com</p>
      <div class="divider lower"></div>
      <div class="card-band"><span class="website">www.tessanoverseas.com</span></div>
    </section>

    <section class="card brand-card" aria-label="Brand side">
      <div class="brand-lockup">
        <span class="brand-dot"></span>
        <span class="brand-name">Tessan Overseas</span>
      </div>
      <div class="card-band"><span class="website">www.tessanoverseas.com</span></div>
    </section>
  </main>
</body>
</html>
```